we need PDF and print ready letterheads, dupplicated 5 times with different company details of different companies. All the companies are Ridgeline Estates and no need for fancy logos (any reasonable shape is ok). Then simply change the companies details (names and company number) and the colour scheme slightly. I will supply the details.

The print ready should be 300dpi, and must have cropped marks.

Should be an easy job!

```html
<!DOCTYPE html>
<html lang="en">
<head>
<meta charset="utf-8">
<title>Ridgeline Estates – Letterhead (print ready)</title>
<link href="https://fonts.googleapis.com/css2?family=Rubik:ital,wght@0,400;0,500;0,700;1,500;1,700&display=swap" rel="stylesheet">
<style>
  :root{
    --backdrop:#dcdcdc;
    --paper:#f5f5f5;
    --brand-red:#a5141c;
    --brand-dark:#2e2e32;
    --ink:#3a3a3a;
    --crop:#1a1a1a;
  }
  *{margin:0;padding:0;box-sizing:border-box}
  html,body{width:1200px;height:1013px;overflow:hidden;background:var(--backdrop)}
  body{font-family:"Rubik",sans-serif;position:relative}

  .crop-marks{position:absolute;left:0;top:0;width:1200px;height:1013px}

  /* bleed area: 9px beyond trim on every side */
  .bleed{
    position:absolute;left:273px;top:43px;width:654px;height:927px;
    background:var(--paper);
  }
  .letterhead{position:absolute;left:9px;top:9px;width:636px;height:909px}
  .edge-band{position:absolute;left:600px;top:-9px;width:45px;height:927px}

  .brand{
    position:absolute;left:46px;top:122px;
    display:flex;align-items:center;gap:11px;
  }
  .brand-mark{width:24px;height:24px;background:var(--brand-red)}
  .brand-name{
    font-weight:700;font-size:27px;line-height:1;color:var(--brand-red);
    letter-spacing:.3px;text-transform:uppercase;
  }

  .contact{position:absolute;right:45px;top:80px;text-align:right}
  .contact-line{
    display:flex;justify-content:flex-end;align-items:center;gap:8px;
    font-weight:500;font-size:14px;line-height:17px;color:#1e1e1e;
  }
  .contact-line svg{width:11px;height:11px;fill:var(--brand-red)}
  .address{
    position:absolute;right:46px;top:146px;text-align:right;
    font-weight:700;font-style:italic;font-size:13.5px;line-height:17px;color:var(--brand-red);
  }

  .heading{
    position:absolute;font-weight:700;font-size:11px;line-height:13px;
    color:var(--brand-red);letter-spacing:.2px;
  }
  .heading--top{left:42px;top:282px}
  .heading--sign{right:63px;top:735px}

  .body-copy{
    position:absolute;left:42px;top:352px;width:534px;
    font-size:7.8px;line-height:10.2px;color:var(--ink);text-align:justify;hyphens:auto;
  }
  .body-copy p{margin-bottom:10px}

  .slogan{
    position:absolute;left:0;width:636px;top:862px;text-align:center;
    font-weight:700;font-style:italic;font-size:18px;line-height:22px;color:var(--brand-dark);
  }
</style>
</head>
<body>
<svg class="crop-marks" viewBox="0 0 1200 1013" aria-hidden="true">
  <g stroke="var(--crop)" stroke-width="0.8">
    <!-- top left -->
    <line x1="248" y1="52" x2="268" y2="52"/><line x1="282" y1="18" x2="282" y2="38"/>
    <!-- top right -->
    <line x1="932" y1="52" x2="952" y2="52"/><line x1="918" y1="18" x2="918" y2="38"/>
    <!-- bottom left -->
    <line x1="248" y1="961" x2="268" y2="961"/><line x1="282" y1="975" x2="282" y2="995"/>
    <!-- bottom right -->
    <line x1="932" y1="961" x2="952" y2="961"/><line x1="918" y1="975" x2="918" y2="995"/>
  </g>
</svg>

<div class="bleed">
  <main class="letterhead">
    <svg class="edge-band" viewBox="0 0 45 927" preserveAspectRatio="none" aria-hidden="true">
      <polygon points="14,0 45,0 45,378 14,419" fill="var(--brand-dark)"/>
      <polygon points="9,435 45,388 45,927 9,927" fill="var(--brand-red)"/>
    </svg>

    <div class="brand">
      <span class="brand-mark"></span>
      <span class="brand-name">Ridgeline Estates</span>
    </div>

    <div class="contact">
      <div class="contact-line">012 345 678
        <svg viewBox="0 0 24 24"><path d="M6.6 10.8a15.1 15.1 0 0 0 6.6 6.6l2.2-2.2a1 1 0 0 1 1-.25 11.4 11.4 0 0 0 3.6.57 1 1 0 0 1 1 1V20a1 1 0 0 1-1 1A17 17 0 0 1 3 4a1 1 0 0 1 1-1h3.5a1 1 0 0 1 1 1c0 1.25.2 2.45.57 3.570a1 1 0 0 1-.25 1z"/></svg>
      </div>
      <div class="contact-line">email@domain.com
        <svg viewBox="0 0 24 24"><path d="M12 2a10 10 0 1 0 0 20 10 10 0 0 0 0-20zm6.9 6h-3a15.7 15.7 0 0 0-1.4-3.6A8 8 0 0 1 18.9 8zM12 4c.8 1.2 1.5 2.5 1.9 4h-3.8c.4-1.5 1.1-2.8 1.9-4zM4.3 14a8 8 0 0 1 0-4h3.4a16 16 0 0 0 0 4zm.8 2h3a15.7 15.7 0 0 0 1.4 3.6A8 8 0 0 1 5.1 16zm3-8h-3a8 8 0 0 1 4.4-3.6A15.7 15.7 0 0 0 8.1 8zM12 20c-.8-1.2-1.5-2.5-1.9-4h3.8c-.4 1.5-1.1 2.8-1.9 4zm2.3-6H9.7a14.6 14.6 0 0 1 0-4h4.6a14.6 14.6 0 0 1 0 4zm.2 5.6a15.7 15.7 0 0 0 1.4-3.6h3a8 8 0 0 1-4.4 3.6zm1.8-5.6a16 16 0 0 0 0-4h3.4a8 8 0 0 1 0 4z"/></svg>
      </div>
      <div class="contact-line">www.website.com
        <svg viewBox="0 0 24 24"><path d="M2 5h20v14H2zm2 2v.5l8 5 8-5V7zm0 2.8V17h16V9.8l-8 5z"/></svg>
      </div>
    </div>

    <div class="address">218 Alder Street,<br>Brookvale, CA 9410</div>

    <h2 class="heading heading--top">LOREM IPSUM</h2>

    <section class="body-copy">
      <p>Lorem ipsum dolor sit amet, consectetur adipiscing elit. Nam ultrices turpis et ex tempor viverra. Orci varius natoque penatibus et magnis dis parturient montes, nascetur ridiculus mus. In hendrerit neque sed nibh accumsan consequat. Nam placerat ut ligula eu accumsan. In nec tristique ipsum, ut ultrices lectus. Praesent at ex vel massa sodales pulvinar. Fusce bibendum consequat odio, nec dapibus arcu vestibulum quis. Proin tristique magna suscipit pulvinar euismod. Nam accumsan augue ac dolor dictum porta. Praesent ut ex congue ligula convallis elementum sit amet vitae lorem. Mauris faucibus mattis aliquet. Morbi feugiat vestibulum condimentum. In quis nisl id purus laoreet vehicula. Aliquam consequat mauris et dolor pretium, ac placerat urna iaculis. Integer blandit nulla dui, sed porta purus maximus quis.</p>
      <p>Curabitur libero odio, sollicitudin a nisl at, rutrum dapibus augue. Sed id nibh bibendum, interdum ipsum in, porttitor mi. Vivamus hendrerit maximus tellus eget scelerisque. Nulla placerat sem feugiat nisl viverra, sed maximus turpis sagittis. Vestibulum ante ipsum primis in faucibus orci luctus et ultrices posuere cubilia Curae; Nulla facilisi. Etiam faucibus non diam vitae lobortis. Morbi consequat nunc ac magna consectetur, eu tempus tellus mattis. Etiam tristique arcu quis velit rutrum, sit amet porta augue condimentum. Aliquam sollicitudin libero vitae enim rutrum egestas. Mauris fringilla nisi lectus, sed tempus ante condimentum blandit. Ut tempor sed urna in dignissim. Donec accumsan pulvinar velit, sed tempor augue commodo eu. In non ex varius metus pellentesque aliquam. In facilisis nibh libero, at malesuada arcu dapibus et. Proin tellus diam, elementum vel quam eget, pellentesque sodales nisi.</p>
      <p>Integer cursus eros a posuere pellentesque. Ut ornare lectus mauris. Maecenas sagittis turpis ac nulla lacinia dapibus vel a orci. Etiam vel pharetra dolor. Nunc vitae tortor in lacus auctor pharetra. Aenean eleifend, nibh at consequat sodales, purus mi vehicula sem, bibendum tristique ipsum tellus eu odio. Nulla facilisi. Nunc fermentum ante a felis rhoncus, quis tempor felis commodo. Phasellus convallis et libero sed hendrerit. Phasellus quis lorem a sem iaculis blandit. Cras vehicula ante quis tortor porttitor, eget sagittis arcu tincidunt. Proin tempus lectus at dolor molestie, vitae elementum sapien sodales.</p>
      <p>Donec eget erat mollis, maximus lorem viverra, ultrices lacus. Sed aliquet, ligula venenatis fringilla volutpat, neque risus venenatis tortor, consequat pharetra justo quam id est. Donec consectetur tempor mauris eu ornare. Nunc nec ex placerat, vestibulum ligula a, feugiat mauris. Etiam mattis in purus vel maximus. Sed purus nisi, rhoncus eget ante vel, cursus tincidunt nulla. Praesent ut enim dolor. Maecenas tempus libero neque, quis volutpat lacus rutrum at. Orci varius natoque penatibus et magnis dis parturient montes, nascetur ridiculus mus. Donec non egestas turpis.</p>
      <p>Maecenas scelerisque egestas luctus. Orci varius natoque penatibus et magnis dis parturient montes, nascetur ridiculus mus. Nam iaculis ut urna eget ultricies. Mauris non congue justo. Vestibulum ornare et ex faucibus vehicula. Pellentesque ac velit et purus blandit maximus. Morbi bibendum iaculis condimentum. Nullam rutrum volutpat nisi.</p>
    </section>

    <h2 class="heading heading--sign">LOREM IPSUM</h2>

    <p class="slogan">Slogan Text Goes Here</p>
  </main>
</div>
</body>
</html>
```